Social media app sign-up flow that asks users to give personal info and connect with other apps

Design an interactive, fun, and playful sign-up flow in which you are providing information about you, your interests, and connecting with different API plug-ins such as Fendora, WorkLoop, Tunevo, etc. (using the brand palette attached).

Basic wireframe, and business requirements are also attached.

Target Market(s)

Gen Z + Millennials (ages 22-40)

Font styles to use
Sans Serif

Colors
fbed22
fbee3d
fbf289

Requirements
Must have
• Forms for users to submit their info. Follow the color palette attached.

Connect with Fendora, Connect with WorkLoop, Connect with Tunevo, Connect with Gatherwick buttons
Nice to have
• I like the way you can use cards to submit your information for each category. Interactive card design for providing your info
Should not have
• Basic outdated designs, long forms

```html
<!DOCTYPE html>
<html lang="en">
<head>
<meta charset="utf-8">
<title>Sign-up flow screens</title>
<link rel="stylesheet" href="https://fonts.googleapis.com/css2?family=Roboto:wght@300;400;500;700&display=swap">
<style>
:root{
  --bg:#fec52e;
  --yellow:#ffc62f;
  --cream:#fff2c9;
  --white:#ffffff;
  --ink:#222222;
  --muted:#555555;
  --accent:#ffae12;
  --grey:#f2f2f0;
  --line:#bdbdbd;
  --navy:#3c56a5;
  --blue:#1277c4;
}
*{box-sizing:border-box;margin:0;padding:0}
html,body{width:903px;height:1200px;overflow:hidden}
body{background:var(--bg);font-family:"Roboto",sans-serif;color:var(--ink);position:relative}
.screen{position:absolute;width:248px;height:537px;border-radius:26px;overflow:hidden;background:var(--cream)}
.abs{position:absolute}
.center{left:0;right:0;text-align:center}
.top-band{position:absolute;left:0;top:0;width:100%;background:var(--yellow)}
.sheet{position:absolute;left:0;right:0;bottom:0;background:var(--cream);border-radius:16px 16px 0 0}
.pill{position:absolute;left:13px;width:221px;height:32px;border:1.5px solid var(--yellow);border-radius:16px;background:var(--white);
  display:flex;align-items:center;justify-content:center;gap:7px;font-size:10px}
.dot{width:9px;height:9px;border-radius:50%;background:var(--ink)}
.foot{font-size:8.5px}
.foot b{color:var(--accent);font-weight:500}
.title{font-size:13px;font-weight:500}
.back{position:absolute;left:12px;top:37px;width:14px;height:14px}
.field{position:absolute;left:13px;width:221px;height:36px;background:var(--white);border-radius:18px;padding:6px 18px}
.field small{display:block;font-size:6px;color:var(--muted)}
.field span{font-size:10px;display:flex;align-items:center;gap:6px;margin-top:2px}
.flag{width:14px;height:9px;background:linear-gradient(180deg,#d33 0 20%,#fff 20% 40%,#d33 40% 60%,#fff 60% 80%,#d33 80%);position:relative}
.flag::before{content:"";position:absolute;left:0;top:0;width:6px;height:5px;background:#2a4d9b}
.cta{position:absolute;left:13px;width:221px;height:33px;border-radius:17px;background:var(--yellow);display:flex;align-items:center;justify-content:center;gap:8px;font-size:11.5px;font-weight:500}
.otp{position:absolute;top:230px;width:39px;height:39px;background:var(--white);border-radius:4px;font-size:24px;font-weight:300;display:flex;align-items:center;justify-content:center}
.key{position:absolute;width:30px;margin-left:-15px;text-align:center;font-size:25px;font-weight:300}
.menu{position:absolute;left:13px;top:37px;width:18px;height:13px}
.avatar{position:absolute;left:207px;top:29px;width:28px;height:28px;border-radius:50%;background:linear-gradient(135deg,#f4c9a8,#b5573a)}
.card{position:absolute;width:99px;height:79px;background:var(--white);display:flex;flex-direction:column;align-items:center;justify-content:flex-end;padding-bottom:8px;font-size:11px;line-height:13px;text-align:center;box-shadow:0 1px 3px rgba(0,0,0,.05)}
.card svg{width:30px;height:30px;margin-bottom:4px}
.card .art{width:30px;height:30px;border-radius:6px;margin-bottom:4px}
.chip{position:absolute;height:27px;background:var(--white);border-radius:14px;display:flex;align-items:center;padding:0 8px;gap:5px;font-size:9px;color:var(--muted)}
.chip .x{margin-left:auto;width:10px;height:10px;border-radius:50%;background:#eee;font-size:7px;text-align:center;line-height:10px;color:#999}
.social{position:absolute;top:452px;height:30px;border-radius:15px;color:var(--white);font-size:8.5px;display:flex;align-items:center;justify-content:center}
</style>
</head>
<body>
<svg width="0" height="0" style="position:absolute">
  <defs>
    <symbol id="pin" viewBox="0 0 24 24"><path d="M12 2a7 7 0 0 0-7 7c0 5 7 13 7 13s7-8 7-13a7 7 0 0 0-7-7z" fill="currentColor"/><circle cx="12" cy="9" r="2.6" fill="#fff"/></symbol>
    <symbol id="arrow" viewBox="0 0 14 14"><path d="M13 7H1M6 2 1 7l5 5" fill="none" stroke="#222" stroke-width="1.4"/></symbol>
    <symbol id="burger" viewBox="0 0 18 13"><path d="M0 1h18M0 6.5h18M0 12h18" stroke="#222" stroke-width="1.6"/></symbol>
  </defs>
</svg>

<!-- Welcome -->
<section class="screen" style="left:33px;top:37px">
  <div class="top-band" style="height:240px"></div>
  <div class="abs center" style="top:100px;font-size:25px;font-weight:700">Welcome</div>
  <div class="abs center" style="top:139px;font-size:14px;font-weight:500;color:#5a4410">Let's Get Started</div>
  <div class="sheet" style="top:230px"></div>
  <div class="pill" style="top:248px">I will use Email or Phone</div>
  <div class="pill" style="top:290px"><i class="dot"></i>Continue with Fendora</div>
  <div class="pill" style="top:333px"><i class="dot"></i>Continue with Searchly</div>
  <div class="pill" style="top:375px"><i class="dot"></i>Continue with Orchard</div>
  <div class="pill" style="top:419px"><i class="dot"></i>Continue with WorkLoop</div>
  <div class="abs center foot" style="top:472px">Don't have account? <b>Register Now</b></div>
</section>

<!-- Sign up -->
<section class="screen" style="left:327px;top:37px">
  <div class="top-band" style="height:70px"></div>
  <svg class="back"><use href="#arrow"/></svg>
  <div class="abs center title" style="top:36px">Sign up</div>
  <div class="sheet" style="top:58px"></div>
  <div class="field" style="top:73px"><small>Country/Region</small><span><i class="flag"></i>United States</span>
    <svg class="abs" style="right:16px;top:15px" width="10" height="6"><path d="M1 1l4 4 4-4" fill="none" stroke="#222" stroke-width="1.3"/></svg></div>
  <div class="field" style="top:117px"><small>Phone number</small><span><i class="flag"></i>+1 &nbsp;<b style="font-weight:500">800 555 0142</b></span></div>
  <div class="abs center" style="top:161px;font-size:9px;color:var(--muted)">We will send you one time password (OTP)</div>
  <div class="abs center" style="top:177px;font-size:7.5px;color:var(--accent)">Carrier rates may apply</div>
  <div class="cta" style="top:198px">CONTINUE
    <svg width="12" height="10"><path d="M0 5h11M7 1l4 4-4 4" fill="none" stroke="#222" stroke-width="1.3"/></svg></div>
  <div class="abs" style="left:13px;top:245px;width:221px;height:1px;background:#555"></div>
  <div class="abs center" style="top:240px"><span style="background:var(--cream);padding:0 6px;font-size:9px">OR</span></div>
  <div class="pill" style="top:259px">I will use Email or Phone</div>
  <div class="pill" style="top:300px"><i class="dot"></i>Continue with Fendora</div>
  <div class="pill" style="top:340px"><i class="dot"></i>Continue with Searchly</div>
  <div class="pill" style="top:382px"><i class="dot"></i>Continue with Orchard</div>
  <div class="pill" style="top:423px"><i class="dot"></i>Continue with WorkLoop</div>
  <div class="abs center foot" style="top:472px">Already have an account? <b>Login!</b></div>
</section>

<!-- Verification -->
<section class="screen" style="left:621px;top:37px">
  <div class="top-band" style="height:180px"></div>
  <svg class="back"><use href="#arrow"/></svg>
  <div class="abs center title" style="top:36px">Enter Verification Code</div>
  <div class="abs" style="left:104px;top:78px;width:40px;height:40px;border-radius:50%;background:var(--white)">
    <svg width="40" height="40"><path d="M13 20l5 5 10-10" fill="none" stroke="var(--yellow)" stroke-width="2"/></svg></div>
  <div class="abs center" style="top:124px;font-size:13.5px;font-weight:500;line-height:19px">OTP has been sent to you<br>on your mobile phone</div>
  <div class="sheet" style="top:168px"></div>
  <div class="abs center" style="top:186px;font-size:11px;font-weight:500">Enter OTP Code</div>
  <div class="otp" style="left:31px">8</div>
  <div class="otp" style="left:81px">3</div>
  <div class="otp" style="left:130px"></div>
  <div class="otp" style="left:179px"></div>
  <div class="abs center" style="top:282px;font-size:9px;color:var(--muted)">Didn't receive OTP? <b style="color:var(--accent);font-weight:500">Resend OTP</b></div>
  <div class="key" style="left:62px;top:319px">8</div><div class="key" style="left:124px;top:319px">2</div><div class="key" style="left:180px;top:319px">5</div>
  <div class="key" style="left:62px;top:363px">1</div><div class="key" style="left:124px;top:363px">3</div><div class="key" style="left:180px;top:363px">4</div>
  <div class="key" style="left:62px;top:408px">6</div><div class="key" style="left:124px;top:408px">7</div><div class="key" style="left:180px;top:408px">9</div>
  <div class="key" style="left:124px;top:451px">0</div>
  <svg class="abs" style="left:168px;top:457px" width="25" height="18"><path d="M7 1h17v16H7L1 9z" fill="none" stroke="#222" stroke-width="1.6"/><path d="M11 5l8 8M19 5l-8 8" stroke="#222" stroke-width="1.6"/></svg>
</section>

<!-- Tell me about you (line icons) -->
<section class="screen" style="left:33px;top:622px">
  <svg class="menu"><use href="#burger"/></svg>
  <div class="avatar" role="img" aria-label="Profile photo"></div>
  <div class="abs center" style="top:36px;font-size:15.5px">Welcome</div>
  <div class="abs center" style="top:60px;font-size:22.5px;font-weight:700">Tell me about you</div>
  <div class="card" style="left:22px;top:106px"><svg viewBox="0 0 30 30" fill="none" stroke="var(--yellow)" stroke-width="1.4"><path d="M15 3a8 8 0 0 0-8 8c0 6 8 14 8 14s8-8 8-14a8 8 0 0 0-8-8z"/><circle cx="15" cy="11" r="3"/><path d="M8 25h14"/></svg>Places I've<br>Lived</div>
  <div class="card" style="left:131px;top:106px"><svg viewBox="0 0 30 30" fill="none" stroke="var(--yellow)" stroke-width="1.4"><path d="M2 12l13-6 13 6-13 6z"/><path d="M8 15v6c4 3 10 3 14 0v-6M27 12v8"/></svg>Schools I've<br>Attended</div>
  <div class="card" style="left:22px;top:201px"><svg viewBox="0 0 30 30" fill="none" stroke="var(--yellow)" stroke-width="1.4"><rect x="3" y="9" width="24" height="17" rx="2"/><path d="M11 9V5h8v4M3 15h24"/></svg>Places I've<br>Worked</div>
  <div class="card" style="left:131px;top:201px"><svg viewBox="0 0 30 30" fill="none" stroke="var(--yellow)" stroke-width="1.4"><circle cx="15" cy="8" r="4"/><circle cx="6" cy="11" r="3"/><circle cx="24" cy="11" r="3"/><path d="M8 25c0-6 14-6 14 0M1 22c0-4 6-5 8-3M29 22c0-4-6-5-8-3"/></svg>People<br>I Know</div>
  <div class="card" style="left:22px;top:296px"><svg viewBox="0 0 30 30" fill="none" stroke="var(--yellow)" stroke-width="1.4"><rect x="4" y="5" width="22" height="21" rx="1"/><path d="M4 10h22M9 3v4M21 3v4"/><circle cx="15" cy="18" r="4"/><path d="M13 18l1.5 1.5L17 17"/></svg>Events I've<br>Attended</div>
  <div class="card" style="left:131px;top:296px"><svg viewBox="0 0 30 30" fill="none" stroke="var(--yellow)" stroke-width="1.4"><rect x="4" y="5" width="22" height="21" rx="1"/><path d="M4 10h22M9 3v4M21 3v4M9 15h3M14 15h3M19 15h3M9 19h3M14 19h3M19 19h3"/></svg>Events I'm<br>Attending</div>
  <div class="card" style="left:22px;top:391px"><svg viewBox="0 0 30 30" fill="none" stroke="var(--yellow)" stroke-width="1.4"><circle cx="7" cy="21" r="3"/><path d="M10 21V4l6 4"/><circle cx="20" cy="24" r="3"/><circle cx="27" cy="22" r="2.5"/><path d="M23 24V12l6.5-2v12"/></svg>Music<br>I Love</div>
  <div class="card" style="left:131px;top:391px"><svg viewBox="0 0 30 30" fill="none" stroke="var(--yellow)" stroke-width="1.4"><path d="M3 20l8-8 5 3 6-7 5 5-9 10-6 2zM11 12l4-5M22 8l3-4"/></svg>Teams<br>I Love</div>
</section>

<!-- Tell me about you (colour art) -->
<section class="screen" style="left:327px;top:622px">
  <svg class="menu"><use href="#burger"/></svg>
  <div class="avatar" role="img" aria-label="Profile photo"></div>
  <div class="abs center" style="top:36px;font-size:15.5px">Welcome</div>
  <div class="abs center" style="top:60px;font-size:22.5px;font-weight:700">Tell me about you</div>
  <div class="card" style="left:22px;top:106px"><i class="art" role="img" aria-label="Colour illustration of a map pin" style="background:linear-gradient(180deg,#f2545b,#5aa9e6)"></i>Places I've<br>Lived</div>
  <div class="card" style="left:131px;top:106px"><i class="art" role="img" aria-label="Colour illustration of a graduation cap" style="background:linear-gradient(180deg,#5b3fa8,#f7b267)"></i>Schools I've<br>Attended</div>
  <div class="card" style="left:22px;top:201px"><i class="art" role="img" aria-label="Colour illustration of a briefcase" style="background:linear-gradient(180deg,#8b5a3c,#c7773f)"></i>Places I've<br>Worked</div>
  <div class="card" style="left:131px;top:201px"><i class="art" role="img" aria-label="Colour illustration of a group of people" style="background:linear-gradient(180deg,#f3b58a,#e07b39)"></i>People<br>I Know</div>
  <div class="card" style="left:22px;top:296px"><i class="art" role="img" aria-label="Colour illustration of a calendar with a tick" style="background:linear-gradient(180deg,#3f7be0,#ffc62f)"></i>Events I've<br>Attended</div>
  <div class="card" style="left:131px;top:296px"><i class="art" role="img" aria-label="Colour illustration of a calendar" style="background:linear-gradient(180deg,#ef4d5a,#dfe6f2)"></i>Events I'm<br>Attending</div>
  <div class="card" style="left:22px;top:391px"><i class="art" role="img" aria-label="Colour illustration of music notes" style="background:linear-gradient(135deg,#ffb81c,#2fc0c9)"></i>Music<br>I Love</div>
  <div class="card" style="left:131px;top:391px"><i class="art" role="img" aria-label="Colour illustration of a handshake" style="background:linear-gradient(135deg,#f6c9a4,#e0a176)"></i>Teams<br>I Love</div>
</section>

<!-- Places I've lived -->
<section class="screen" style="left:621px;top:622px">
  <div class="top-band" style="height:69px"></div>
  <svg class="menu"><use href="#burger"/></svg>
  <div class="abs center" style="top:36px;font-size:12px">Places I've Lived</div>
  <div class="avatar" role="img" aria-label="Profile photo"></div>
  <div class="abs" role="img" aria-label="Street map with pinned places" style="left:0;top:69px;width:248px;height:159px;background:linear-gradient(180deg,#eeeeee,#f6f6f6)"></div>
  <div class="abs" style="left:0;top:228px;width:248px;height:94px;background:var(--grey)"></div>
  <div class="chip" style="left:14px;top:244px;width:91px"><svg width="9" height="10" style="color:var(--yellow)"><use href="#pin"/></svg>Chicago<i class="x">×</i></div>
  <div class="chip" style="left:115px;top:244px;width:92px"><svg width="9" height="10" style="color:var(--yellow)"><use href="#pin"/></svg>Madrid<i class="x">×</i></div>
  <div class="chip" style="left:14px;top:280px;width:81px"><svg width="9" height="10" style="color:var(--yellow)"><use href="#pin"/></svg>Paris<i class="x">×</i></div>
  <div class="chip" style="left:105px;top:280px;width:111px"><svg width="9" height="10" style="color:var(--yellow)"><use href="#pin"/></svg>Rio de Janiero<i class="x">×</i></div>
  <div class="abs center" style="top:332px;font-size:13px;font-weight:500">Good Morning, Theo!</div>
  <div class="abs" style="left:14px;top:362px;width:220px;height:27px;background:var(--white);border-radius:14px;display:flex;align-items:center;padding-left:20px;gap:10px;font-size:9.5px;color:var(--muted)"><svg width="9" height="10" style="color:#888"><use href="#pin"/></svg>Lond|</div>
  <div class="abs" style="left:32px;top:390px;width:186px;height:50px;background:var(--white);padding:7px 0 0 18px;font-size:9.5px;line-height:20px">
    <div style="display:flex;gap:6px;align-items:center"><svg width="8" height="10" style="color:#666"><use href="#pin"/></svg><span><b style="font-weight:500">Lond</b>on, United Kingdom</span></div>
    <div style="display:flex;gap:6px;align-items:center"><svg width="8" height="10" style="color:#666"><use href="#pin"/></svg><span><b style="font-weight:500">Lond</b>rina, Parana</span></div>
  </div>
  <div class="social" style="left:14px;width:107px;background:var(--navy)">Login with Fendora</div>
  <div class="social" style="left:127px;width:108px;background:var(--blue)">Login with WorkLoop</div>
</section>
</body>
</html>
```